Website for Veteran Air Force Plumbing Combany

Project:
current site: talvikcrew.com
Growing plumbing company in need of a new homepage and inner page template (2 PSDs). Their goal for their style would be to have distinct areas that direct to their main menu items (Service Areas, Services, Sewer & Drain Cleaning, Blog) (example competitor site: http://larkfieldpipefixers.com/).

Homepage:

Theme: Masculine, Air Force veteran, plumbing, honest up-front pricing, free estimates

1. Style distinct areas
a. Top phone numbers with area served (High priority for customer)
i. Fort Myers: (555) 318-4702
Estero: (555) 318-4702
Naples: (555) 726-1059
Bonita Springs: (555) 726-1059
b. Social Buttons (chatterly, quipster, vidnook, careerloop, zorbo+)
i. Separate Quipster Follow button
c. Logo
d. 24 HR Emergency plumber CTA button
e. Menu
f. Slider with cta buttons
g. Video spot
h. Testimonials
i. Chatterly page plugin spot
j. Quick contact form (email address, small paragraph, send button)
k. Coupons
l. Page Title & Welcome paragraph
m. service columns with action buttons
n. Marla's list & QT Rating action buttons
o. Footer

Inner page:
1. Page title
2. Content section
3. Side bar section
a. video spot
b. Zorbo testimonial plugin spot
c. video2 spot
d. Marla's List & QT Rating action buttons

Target Market(s)

Home owners and construction managers

Industry/Entity Type

It Company

Number of Pages Required

2 page

Requirements
Must have
• Clear distinct areas for information
• Prominent area/phone number

```html
<!DOCTYPE html>
<html lang="en">
<head>
<meta charset="utf-8">
<title>Talvik Crew Plumbing &amp; Drain</title>
<link href="https://fonts.googleapis.com/css2?family=Open+Sans:wght@300;400;600;700;800&display=swap" rel="stylesheet">
<style>
:root{
  --red:#d8312b;
  --slate:#3a4652;
  --slate-dark:#2a333c;
  --nav:#2e3338;
  --orange:#c56a3c;
  --orange-dark:#a9532a;
  --white:#ffffff;
  --ink:#444b52;
  --muted:#8a9096;
  --footer:#23282d;
}
*{box-sizing:border-box;margin:0;padding:0}
html,body{width:1200px;height:3512px;overflow:hidden}
body{font-family:"Open Sans",Arial,sans-serif;color:var(--ink);background:var(--white)}
.page{position:relative;width:1200px;height:3512px}
section,header,nav,footer{position:relative;width:1200px;overflow:hidden}

/* header */
.site-header{height:112px;background:var(--white)}
.brand{position:absolute;left:70px;top:22px;display:flex;align-items:center;gap:14px}
.brand-dot{width:20px;height:20px;background:var(--red)}
.brand-name{font-weight:800;font-size:34px;color:var(--red);line-height:1}
.brand-sub{display:block;font-weight:800;font-size:34px;color:var(--red)}
.header-right{position:absolute;right:70px;top:18px;text-align:right}
.emergency{font-size:16px;color:var(--ink);display:flex;align-items:center;gap:8px;justify-content:flex-end}
.social{display:flex;gap:12px;justify-content:flex-end;margin-top:14px}
.social span{width:16px;height:16px;border-radius:50%;background:var(--red)}

/* nav */
.main-nav{height:48px;background:var(--nav)}
.main-nav ul{list-style:none;display:flex;justify-content:space-between;padding:0 70px;height:48px;align-items:center}
.main-nav li{color:var(--white);font-size:17px}

/* hero */
.hero{height:460px;background:linear-gradient(90deg,#eef0f1,#dfe3e6)}
.hero-badge{position:absolute;left:220px;top:40px;width:170px;height:120px;border-radius:60px;background:linear-gradient(135deg,#6fc14a,#d8312b)}
.hero-text{position:absolute;left:220px;top:198px;width:400px;font-size:22px;line-height:1.45;color:#3a3f44}
.btn-red{display:inline-flex;align-items:center;gap:8px;background:var(--red);color:var(--white);font-size:15px;padding:10px 22px;margin-top:22px;border-radius:2px}
.hero-photo{position:absolute;left:650px;top:0;width:460px;height:460px;background:linear-gradient(180deg,#4c6a8c,#2d4560)}
.dots{position:absolute;left:560px;bottom:24px;display:flex;gap:10px}
.dots span{width:14px;height:14px;border-radius:50%;background:#b8bec3}
.dots span:first-child{background:#555}

/* service bands */
.service{height:420px;color:var(--white)}
.service.dark{background:linear-gradient(160deg,var(--slate),var(--slate-dark))}
.service.orange{background:linear-gradient(160deg,var(--orange),var(--orange-dark))}
.service-photo{position:absolute;top:80px;width:290px;height:260px;border-radius:8px;background:linear-gradient(135deg,#8ea6bd,#4b6580)}
.orange .service-photo{background:linear-gradient(135deg,#8b6a4a,#4c3a28)}
.service-copy{position:absolute;top:50px;width:560px}
.service h2{font-weight:300;font-size:42px;margin-bottom:26px;line-height:1.2}
.service p{font-size:14px;line-height:1.75}
.btn-outline{display:inline-block;border:1px solid var(--white);color:var(--white);font-size:15px;padding:10px 26px;margin-top:26px}
.btn-solid-white{display:inline-block;background:var(--white);color:var(--ink);font-size:15px;padding:10px 26px;margin-top:26px}

/* who */
.who{height:352px;text-align:center;padding-top:50px}
.who h2{color:var(--red);font-weight:400;font-size:42px}
.who p{width:920px;margin:28px auto 0;font-size:14px;line-height:1.75;color:var(--ink)}
.btn-red-outline{display:inline-block;border:1px solid var(--red);color:var(--red);font-size:15px;padding:10px 28px;margin-top:30px}

/* testimonials */
.testimonials{height:508px;background:linear-gradient(180deg,#3e4952,#2a3239);color:var(--white);text-align:center;padding-top:36px}
.testimonials h2{font-weight:300;font-size:42px}
.quotes{display:flex;justify-content:space-between;padding:0 80px;margin-top:60px}
.quote{width:300px}
.avatar{width:64px;height:64px;border-radius:50%;margin:0 auto 22px;background:#c9cdd1;border:3px solid var(--white)}
.quote p{font-size:14px;line-height:1.7}
.quote .who-name{margin-top:26px;font-size:14px;color:#c7ccd0}

/* video */
.video{height:340px}
.video-thumb{position:absolute;left:112px;top:12px;width:368px;height:240px;background:linear-gradient(135deg,#b8c2cb,#6d7b88)}
.play{position:absolute;left:260px;top:100px}
.video-copy{position:absolute;left:530px;top:12px;width:560px}
.video-copy h3{color:var(--red);font-weight:400;font-size:22px}
.video-copy p{font-size:14px;line-height:1.75;margin-top:18px}
.video-copy .btn-red-outline{margin-left:70px}

/* contact */
.contact{height:300px;background:linear-gradient(160deg,var(--orange),var(--orange-dark));color:var(--white)}
.contact h2{position:absolute;left:0;right:0;top:26px;text-align:center;font-weight:300;font-size:42px}
.field{position:absolute;background:var(--white);height:28px;font-size:12px;color:var(--muted);padding:6px 10px}
.send{position:absolute;left:250px;top:228px;width:160px;height:36px;background:var(--white);color:var(--ink);font-size:15px;text-align:center;line-height:36px}
.side-btn{position:absolute;left:870px;width:190px;height:40px;border:1px solid var(--white);font-size:14px;line-height:40px;padding-left:16px;color:var(--white)}
.sq{position:absolute;left:800px;width:54px;height:44px;background:var(--white)}
.call{position:absolute;left:0;right:0;top:218px;text-align:center;font-size:15px;line-height:1.55}
.call strong{font-weight:700}

/* footer */
.site-footer{height:132px;background:var(--footer);text-align:center;color:#9aa0a5}
.foot-brand{padding-top:22px;display:flex;justify-content:center;align-items:center;gap:10px}
.foot-brand .brand-name{font-size:24px}
.site-footer .social{justify-content:center;margin-top:14px}
.copy{font-size:11px;margin-top:12px}
</style>
</head>
<body>
<div class="page">

<header class="site-header">
  <div class="brand">
    <span class="brand-dot"></span>
    <div class="brand-name">TALVIK CREW<span class="brand-sub">PLUMBING &amp; DRAIN</span></div>
  </div>
  <div class="header-right">
    <div class="emergency">
      <svg width="16" height="16" viewBox="0 0 24 24"><path fill="#d8312b" d="M6.6 10.8a15 15 0 006.6 6.6l2.2-2.2c.3-.3.7-.4 1-.2 1.1.4 2.3.6 3.6.6.6 0 1 .4 1 1V20c0 .6-.4 1-1 1A17 17 0 013 4c0-.6.4-1 1-1h3.5c.6 0 1 .4 1 1 0 1.3.2 2.5.6 3.6.1.3 0 .7-.2 1z"/></svg>
      24hr Emergency Plumber
    </div>
    <div class="social"><span></span><span></span><span></span><span></span><span></span></div>
  </div>
</header>

<nav class="main-nav">
  <ul><li>Home</li><li>About us</li><li>Services</li><li>Sewer &amp; Drain Cleaning</li><li>Products</li><li>Blog</li><li>Contact Us</li></ul>
</nav>

<section class="hero">
  <div class="hero-badge" role="img" aria-label="24/7 service badge graphic"></div>
  <div class="hero-text">
    Get the best plumbing service for drain cleaning, leaky faucets, toilet repair, and clogged drains.<br>
    <span class="btn-red">
      <svg width="14" height="14" viewBox="0 0 24 24"><path fill="#fff" d="M6.6 10.8a15 15 0 006.6 6.6l2.2-2.2c.3-.3.7-.4 1-.2 1.1.4 2.3.6 3.6.6.6 0 1 .4 1 1V20c0 .6-.4 1-1 1A17 17 0 013 4c0-.6.4-1 1-1h3.5c.6 0 1 .4 1 1 0 1.3.2 2.5.6 3.6.1.3 0 .7-.2 1z"/></svg>
      Call Now</span>
  </div>
  <div class="hero-photo" role="img" aria-label="Photo of the two plumbing company owners in uniform shirts"></div>
  <div class="dots"><span></span><span></span><span></span></div>
</section>

<section class="service dark">
  <div class="service-photo" style="left:112px" role="img" aria-label="Photo of a plumber servicing a water heater"></div>
  <div class="service-copy" style="left:530px">
    <h2>Water Heater Repair &amp; Installation</h2>
    <p>Your water heater is one of the hardest working appliances in your home. Yet it is out of sight and mind until it stops heating water or starts leaking onto your floors. Here in Southwest Florida, you should plan on replacing your water heater when it reaches the age of ten years old.</p>
    <div style="text-align:right"><span class="btn-solid-white">Read More</span></div>
  </div>
</section>

<section class="service orange">
  <div class="service-copy" style="left:76px;width:600px">
    <h2>Garbage Disposals</h2>
    <p>If you are experiencing a problem with your garbage disposal, there are a few things you can do before calling for plumbing service. A jammed flywheel is the most common problem associated with garbage disposal service calls. Your disposal's flywheel is the spinning section you can see by looking past the rubber gasket.</p>
    <span class="btn-outline">Read More</span>
  </div>
  <div class="service-photo" style="left:760px" role="img" aria-label="Photo of hands repairing a garbage disposal under a sink"></div>
</section>

<section class="service dark">
  <div class="service-photo" style="left:112px" role="img" aria-label="Photo of a plumber working under a kitchen sink"></div>
  <div class="service-copy" style="left:530px">
    <h2>Kitchen &amp; Bathroom Remodeling Plumber</h2>
    <p>We are a licensed and insured kitchen and bathroom remodeling plumber in Southwest Florida. No matter how small or large your project is, we are the premier plumbers in Fort Myers, Naples, Estero, Bonita Springs and San Carlos Park.</p>
    <div style="text-align:right"><span class="btn-outline">Read More</span></div>
  </div>
</section>

<section class="who">
  <h2>Who We Are</h2>
  <p>Talvik Crew Plumbing &amp; Drain is a veteran owned and operated local plumbing service in Southwest Florida. We pride our self on military core values of honesty, integrity, and excellence in all we do. We will arrive on time, clean up any mess we make, and warranty our work. The brothers are originally from the Midwest but have been serving Southwest Florida for over thirteen years.</p>
  <span class="btn-red-outline">Read More</span>
</section>

<section class="testimonials">
  <h2>What our Customers Say</h2>
  <div class="quotes">
    <div class="quote"><div class="avatar" role="img" aria-label="Customer portrait"></div><p>Lorem Ipsum is simply dummy text of the printing and typesetting industry.</p><div class="who-name">Alex</div></div>
    <div class="quote"><div class="avatar" role="img" aria-label="Customer portrait"></div><p>It takes a little more than your traditional plumbers to solve a home leak and afford all your trust.</p><div class="who-name">Ruben Ash</div></div>
    <div class="quote"><div class="avatar" role="img" aria-label="Customer portrait"></div><p>Lorem Ipsum is simply dummy text of the printing and typesetting industry.</p><div class="who-name">Mara</div></div>
  </div>
</section>

<section class="video">
  <div class="video-thumb" role="img" aria-label="Video still of a plumber talking about services"></div>
  <svg class="play" width="72" height="72" viewBox="0 0 72 72"><circle cx="36" cy="36" r="34" fill="#fff" opacity=".9"/><path d="M29 22l22 14-22 14z" fill="#333"/></svg>
  <div class="video-copy">
    <h3>5 star plumber in Estero, FL|Talvik Crew Plumbing</h3>
    <p>Our plumbers in Naples are some of the best our area has to offer, they are not paid commission so you can trust your diagnosis to be only what is needed. You can trust our plumbers to be honest, dependable and affordable.</p>
    <span class="btn-red-outline">View More Video</span>
  </div>
</section>

<section class="contact">
  <h2>Get in Touch with us</h2>
  <div class="field" style="left:112px;top:100px;width:120px">Name</div>
  <div class="field" style="left:112px;top:138px;width:120px">Email Id</div>
  <div class="field" style="left:112px;top:176px;width:120px">Subject</div>
  <div class="field" style="left:250px;top:100px;width:280px;height:104px">Message</div>
  <div class="send">Send</div>
  <div class="sq" style="top:92px"></div>
  <div class="side-btn" style="top:94px">Follow us on Quipster</div>
  <div class="sq" style="top:148px"></div>
  <div class="side-btn" style="top:150px">Go To Map</div>
  <div class="call"><strong>Call us On Following Contacts</strong><br>Fort Myers<br>(555) 318-4702</div>
</section>

<footer class="site-footer">
  <div class="foot-brand"><span class="brand-dot" style="width:14px;height:14px"></span><span class="brand-name">TALVIK CREW PLUMBING &amp; DRAIN</span></div>
  <div class="social"><span></span><span></span><span></span><span></span><span></span></div>
  <div class="copy">© 2016, All Rights Reserved</div>
</footer>

</div>
</body>
</html>
```